Corporate Letterhead

Looking for a new corporate letterhead design. Our colors are orange and gray.

We'd like it if the below could be included somehow in the letterhead.                                       

Integrity | Service | Value

• Logo, Company Name, Address, Phone #, Fax #, Web address, Email address (optional), the phrase "A Service Disable Veteran Owned Small Business".

```html
<!DOCTYPE html>
<html lang="en">
<head>
<meta charset="utf-8">
<title>Veridan Systems — Letterhead</title>
<link rel="stylesheet" href="https://fonts.googleapis.com/css2?family=Open+Sans:wght@400;600;700;800&family=Great+Vibes&display=swap">
<style>
  :root {
    --orange: #e8902a;
    --gray: #8b8c8e;
    --ink: #4a4a4c;
    --paper: #ffffff;
    --backdrop: #ececec;
    --footer-text: #f2f2f2;
  }
  * { margin: 0; padding: 0; box-sizing: border-box; }
  html, body { width: 1200px; height: 795px; overflow: hidden; }
  body {
    background: var(--backdrop);
    font-family: "Open Sans", Arial, sans-serif;
    color: var(--ink);
  }
  .letterhead {
    position: absolute;
    left: 319px; top: 0;
    width: 562px; height: 795px;
    background: var(--paper);
    overflow: hidden;
  }
  .brand {
    position: absolute; left: 46px; top: 62px;
    display: flex; align-items: center; gap: 10px;
  }
  .brand-dot {
    width: 30px; height: 30px; border-radius: 50%;
    background: var(--orange);
  }
  .brand-name {
    font-weight: 800; font-size: 18px; line-height: 1;
    color: var(--orange); letter-spacing: .5px;
  }
  .tagline {
    font-weight: 600; font-size: 8.5px; color: var(--gray);
    margin-top: 5px; letter-spacing: .3px;
  }
  .letter {
    position: absolute; left: 96px; top: 166px; width: 380px;
    font-size: 8.4px; line-height: 1.45;
  }
  .salutation { font-weight: 700; margin-bottom: 12px; }
  .letter p { margin-bottom: 12px; }
  .signature { margin-top: 30px; }
  .signature-script {
    font-family: "Great Vibes", cursive; font-size: 30px; color: #222;
    line-height: 1;
  }
  .signature-title { font-weight: 700; font-size: 8.5px; margin-top: 2px; }
  .footer-art { position: absolute; left: 0; top: 0; }
  .footer-contact {
    position: absolute; left: 60px; top: 752px;
    display: flex; gap: 16px; color: var(--footer-text);
    font-size: 7.5px; line-height: 1.35;
  }
  .footer-contact .divider { width: 1px; background: var(--footer-text); opacity: .8; }
  .veteran-note {
    position: absolute; right: 22px; top: 690px; width: 140px;
    color: var(--footer-text); font-size: 7.5px; letter-spacing: .8px;
    text-align: right; line-height: 1.35;
  }
</style>
</head>
<body>
  <main class="letterhead">
    <header class="brand">
      <span class="brand-dot"></span>
      <div>
        <div class="brand-name">VERIDAN SYSTEMS, INC</div>
        <div class="tagline">Integrity | Service | Value</div>
      </div>
    </header>

    <section class="letter">
      <div class="salutation">Lorem Ipsum,</div>
      <p>Cras mattis consectetur purus sit amet fermentum. Etiam porta sem malesuada magna mollis euismod. Integer posuere erat a ante venenatis dapibus posuere velit aliquet. Cras justo odio, dapibus ac facilisis in, egestas eget quam. Aenean eu leo quam. Pellentesque ornare sem lacinia quam venenatis vestibulum.</p>
      <p>Vivamus sagittis lacus vel augue laoreet rutrum faucibus dolor auctor. Donec sed odio dui. Etiam porta sem malesuada magna mollis euismod. Morbi leo risus, porta ac consectetur ac, vestibulum at eros. Nullam id dolor id nibh ultricies vehicula ut id elit.</p>
      <p>Donec id elit non mi porta gravida at eget metus. Fusce dapibus, tellus ac cursus commodo, tortor mauris condimentum nibh, ut fermentum massa justo sit amet risus. Cras justo odio, dapibus ac facilisis in, egestas eget quam. Cum sociis natoque penatibus et magnis dis parturient montes, nascetur ridiculus mus.</p>
      <p>Cum sociis natoque penatibus et magnis dis parturient montes, nascetur ridiculus mus. Curabitur blandit tempus porttitor. Aenean lacinia bibendum nulla sed consectetur. Lorem ipsum dolor sit amet, consectetur adipiscing elit.</p>
      <p>Cras justo odio, dapibus ac facilisis in, egestas eget quam. Morbi leo risus, porta ac consectetur ac, vestibulum at eros. Duis mollis, est non commodo luctus, nisi erat porttitor ligula, eget lacinia odio sem nec elit. Integer posuere erat a ante venenatis dapibus posuere velit aliquet. Vivamus sagittis lacus vel augue laoreet rutrum faucibus dolor auctor.</p>
      <div class="signature">
        <div class="signature-script">Your Name</div>
        <div class="signature-title">Company Director</div>
      </div>
    </section>

    <svg class="footer-art" width="562" height="795" viewBox="0 0 562 795" aria-hidden="true">
      <path d="M0 795 L0 740 C 240 734 450 680 562 566 L562 795 Z" fill="var(--gray)"/>
      <path d="M0 740 C 240 734 450 680 562 566 L562 557 C 450 673 240 728 0 734 Z" fill="var(--orange)"/>
    </svg>

    <footer class="footer-contact">
      <div>24 Harbor Point Road<br>Country 204518</div>
      <span class="divider"></span>
      <div>T 555 01 2468<br>F 555 01 2469</div>
      <span class="divider"></span>
      <div>info@veridan.com<br>www.veridan.com</div>
    </footer>
    <div class="veteran-note">A Service Disable Veteran Owned Small Business</div>
  </main>
</body>
</html>
```